Chauffeur Service Presentation folder with 4 side flyer

Things to consider when creating the design,
- I do not want it to look like my old brochure which looks boring and relates to the industry for example we don’t need to use pictures of cars or pictures of a Chauffeur opening a door. etc… Just want it to look modern and creative. Something simple and minimalisitic. If you have any ideas I am happy to let you suggest something.

PRESENTATION FOLDER
-Presentation folder will be prepared to fit A4 size flyer into the inside sleeve.
Clean and simple look. FILE 1 ""EXAMPLE OF FOLDER.PNG""
like the clean look of this folder FILE 4 "EXAMPLE OF FOLDER 2""

-would prefer to use white as the main color

Trying to maintain a similar colour pallet as my company pallet.
FILE 2 ""CHAUFFEURED COLOR PALLETE""

-BROCHURE FLYER

- will fit into the internal sleeve of presentation folder, will need 4 sides to to the flyer with 1 fold. example
FILE 8 "'BROCHURE FOLDED ""

-I have also attached the old brochure we had which is really outdated, just a guide for you to see what we had. FILE 3 ""PROFILE 2013 TKPORTAL""

-Relate to the color scheme we have used for Logo and business card attached in color palette. I have higher res for you if you want me to forward to you.

-Could use some illustration/ icons in the place of images for service provided etc,
FILE 5 ""IDEA FOR SERVICE TYPES""

Listing my service types like below on front page or inside there flyer or even on the presentation folder?
FILE 6 ""LIST OF SERVICES""
Corporate transfer, Airport transfer, vip service, door to door service,
I can provide a list to create

The Layout inside, I am not to fussed as long as it is clean looking,
Maybe we can use the business color scheme throughout while changing font colors and make some parts inversed by using white text with the color boxed over it?

example of white text with coloured box and also different types of font
FILE 7 ""IDEAS""

```html
<!DOCTYPE html>
<html lang="en">
<head>
<meta charset="utf-8">
<title>Velvet Route – Presentation Folder</title>
<link rel="stylesheet" href="https://fonts.googleapis.com/css2?family=Oswald:wght@300;400;600&family=Open+Sans:wght@400;600&family=Roboto+Slab:wght@700&family=Archivo+Black&family=Tinos&family=Lora:ital@1&family=Lato:wght@400&display=swap">
<style>
  :root {
    --pink: #e03a5a;
    --black: #141414;
    --charcoal: #3a3a3a;
    --beige: #ece0d4;
    --white: #ffffff;
    --backdrop: #dcdcdc;
    --line: #2a2a2a;
  }
  * { box-sizing: border-box; margin: 0; padding: 0; }
  html, body { width: 1200px; height: 968px; overflow: hidden; }
  body { background: var(--backdrop); position: relative; font-family: "Open Sans", sans-serif; }

  .folder-panel { position: absolute; top: 213px; height: 676px; background: var(--white); border: 1px solid var(--line); }
  .folder-panel--left { left: 124px; width: 478px; background: linear-gradient(90deg, var(--white) 70%, #ededed 100%); border-right: none; }
  .folder-panel--right { left: 602px; width: 474px; border-left: none; }

  .flyer { position: absolute; left: 614px; top: 78px; width: 450px; height: 640px; background: var(--white); box-shadow: 0 0 0 1px #d0d0d0; overflow: hidden; }
  .flyer__bar { position: absolute; left: 72px; top: 38px; width: 352px; height: 11px; background: var(--pink); }
  .flyer__brand { position: absolute; left: 0; right: 0; top: 70px; text-align: center; font-family: "Oswald", sans-serif; font-weight: 600; font-size: 34px; color: var(--charcoal); letter-spacing: 1px; }
  .flyer__rule { position: absolute; left: 60px; right: 22px; top: 128px; height: 1px; background: var(--line); }

  .tagline { position: absolute; left: 62px; top: 140px; width: 178px; font-family: "Oswald", sans-serif; font-weight: 400; color: var(--black); font-size: 27px; line-height: 32px; }
  .tagline span { display: block; white-space: nowrap; }
  .tagline .t1 { letter-spacing: 0.5px; }
  .tagline .t2 { letter-spacing: 6px; }
  .tagline .t3 { letter-spacing: 17px; }
  .tagline .t4 { letter-spacing: 9px; }
  .flyer__divider { position: absolute; left: 244px; top: 135px; width: 1px; height: 255px; background: var(--line); }
  .flyer__frame-left { position: absolute; left: 60px; top: 135px; width: 1px; height: 255px; background: var(--line); }
  .flyer__frame-right { position: absolute; left: 444px; top: 135px; width: 1px; height: 255px; background: var(--line); }
  .car-illustration { position: absolute; left: 66px; top: 282px; width: 160px; height: 92px; background: linear-gradient(135deg, #f6d5dc, #ecb3bf); border-radius: 4px; }

  .promise { position: absolute; left: 252px; top: 150px; width: 186px; height: 90px; background: var(--pink); color: var(--white); font-family: "Oswald", sans-serif; }
  .promise__top { position: absolute; left: 8px; top: 2px; font-size: 34px; font-weight: 300; letter-spacing: 0.5px; }
  .promise__and { position: absolute; right: 6px; top: 10px; width: 56px; height: 34px; border-radius: 50%; background: var(--beige); color: var(--pink); font-size: 22px; text-align: center; line-height: 32px; font-weight: 400; }
  .promise__bottom { position: absolute; left: 8px; top: 44px; font-size: 33px; font-weight: 600; letter-spacing: 0.5px; }
  .promise-quote { position: absolute; left: 252px; top: 248px; width: 186px; text-align: center; font-size: 16.5px; line-height: 22px; color: var(--black); }

  .band { position: absolute; left: 48px; top: 390px; width: 398px; height: 48px; background: var(--black); color: var(--beige); font-family: "Oswald", sans-serif; font-weight: 300; font-size: 28px; letter-spacing: 3px; text-align: center; line-height: 46px; }
  .pride-quote { position: absolute; left: 52px; top: 444px; width: 392px; text-align: center; font-size: 16.5px; color: var(--black); }
  .pride-quote span { display: block; line-height: 27px; border-bottom: 1px solid var(--line); }
  .pride-quote span:last-child { border-bottom: none; }

  .flyer__wave { position: absolute; left: 0; top: 536px; width: 450px; height: 70px; }
  .emblem { position: absolute; left: 150px; top: 540px; width: 110px; height: 34px; border-radius: 17px; background: linear-gradient(180deg, #d8d8d8, #8d8d8d); }

  .pocket { position: absolute; left: 600px; top: 630px; width: 476px; height: 259px; }
  .service { position: absolute; white-space: nowrap; line-height: 1; }
  .service--door { left: 725px; top: 710px; font-family: "Roboto Slab", serif; font-weight: 700; font-size: 29px; color: var(--black); }
  .service--transfer { left: 726px; top: 742px; font-family: "Roboto Slab", serif; font-weight: 700; font-size: 33px; color: var(--white); }
  .service--vip { left: 925px; top: 730px; font-family: "Lato", sans-serif; font-size: 64px; color: var(--beige); }
  .service--daily { left: 725px; top: 780px; font-family: "Archivo Black", sans-serif; font-size: 23px; letter-spacing: 2px; color: var(--black); }
  .service--tailored { left: 725px; top: 803px; font-family: "Tinos", serif; font-size: 30px; color: var(--black); }
  .service--corporate { left: 730px; top: 834px; font-family: "Lora", serif; font-style: italic; font-size: 38px; color: var(--beige); }
  .service--airport { left: 690px; top: 740px; writing-mode: vertical-rl; font-family: "Archivo Black", sans-serif; font-size: 30px; color: var(--white); }
  .service--vertical { left: 1040px; top: 712px; writing-mode: vertical-rl; transform: rotate(180deg); font-family: "Lato", sans-serif; font-size: 26px; color: var(--beige); }
</style>
</head>
<body>
  <div class="folder-panel folder-panel--left"></div>
  <div class="folder-panel folder-panel--right"></div>

  <article class="flyer">
    <div class="flyer__bar"></div>
    <div class="flyer__brand">Velvet Route</div>
    <div class="flyer__rule"></div>

    <div class="flyer__frame-left"></div>
    <div class="flyer__divider"></div>
    <div class="flyer__frame-right"></div>

    <h2 class="tagline">
      <span class="t1">THE LEADERS IN</span>
      <span class="t2">CHAUFFEUR</span>
      <span class="t3">DRIVEN</span>
      <span class="t4">SERVICE</span>
    </h2>
    <div class="car-illustration" role="img" aria-label="Line illustration of a classic luxury car in red"></div>

    <div class="promise">
      <span class="promise__top">RELIABLE</span>
      <span class="promise__and">and</span>
      <span class="promise__bottom">SUFFICIENT</span>
    </div>
    <p class="promise-quote">“Rely on<br>Velvet Route<br>to provide<br>your luxury<br>transport needs<br>Australia wide.”</p>

    <div class="band">superior and professional</div>
    <p class="pride-quote">
      <span>“We take great pride in providing our clients</span>
      <span>with superior and professional service by</span>
      <span>making no detail too small to cater for.”</span>
    </p>

    <svg class="flyer__wave" viewBox="0 0 450 70" aria-hidden="true">
      <path d="M0,14 C80,0 150,4 230,22 C300,38 380,36 450,24 L450,40 C380,52 300,54 230,38 C150,20 80,16 0,30 Z" fill="var(--black)"/>
      <path d="M0,34 C80,20 150,24 230,42 C300,58 380,56 450,44 L450,58 C380,70 300,70 230,56 C150,40 80,36 0,50 Z" fill="var(--beige)"/>
    </svg>
    <div class="emblem" role="img" aria-label="Silver winged car emblem ornament"></div>
  </article>

  <svg class="pocket" viewBox="0 0 476 259" aria-hidden="true">
    <path d="M0,259 L0,130 C40,50 120,8 210,2 L476,2 L476,259 Z" fill="var(--pink)"/>
  </svg>

  <ul class="services" style="list-style:none">
    <li class="service service--door">door to door service</li>
    <li class="service service--transfer">transfer</li>
    <li class="service service--vip">vip</li>
    <li class="service service--daily">daily hire</li>
    <li class="service service--tailored">TAILORED SERVICES</li>
    <li class="service service--corporate">Corporate transfer</li>
    <li class="service service--airport">Airport</li>
    <li class="service service--vertical">service</li>
  </ul>
</body>
</html>
```